High-end residential home builder needs a business card design

We need a new business card design for a small residential construction company based in Boise, Idaho. We specialize in building custom high-end homes and remodels, with a focus on great design and craftsmanship.

We would like to use our current logo, but open to new color suggestions.
Just looking for a clean, sharp, modern design that looks high-end.

Target Market(s)

Upscale clientele

Industry/Entity Type

Contractor

Contact Information for Business Card

Company: Stonehaven Custom Builders
Name: Colin Marsh
Phone number: 208 637 4120
Email: ColinMarshSCB@quillpost.net
Website: Stonehavencustombuilders.com

Font styles to use
Serif
Sans Serif

Requirements
Must have
• Company Logo
Company name
My name
My phone number
My email
Company website
Nice to have
• I have attached a few photos of cards that I really like.

```html
<!DOCTYPE html>
<html lang="en">
<head>
<meta charset="utf-8">
<title>Stonehaven Custom Builders — Business Card</title>
<link rel="stylesheet" href="https://fonts.googleapis.com/css2?family=Roboto+Condensed:wght@400;700&display=swap">
<style>
  :root {
    --backdrop: #b9bcbc;
    --paper: #f4f3f0;
    --ink: #1e1b19;
    --ink-soft: #4a4846;
    --amber: #e39a1e;
    --edge: #c98a22;
  }
  * { margin: 0; padding: 0; box-sizing: border-box; }
  html, body {
    width: 1200px; height: 824px; overflow: hidden;
    background: var(--backdrop);
    font-family: "Roboto Condensed", "Arial Narrow", sans-serif;
  }
  .stage {
    width: 1200px; height: 824px;
    display: flex; align-items: center; justify-content: center; gap: 60px;
  }
  .card {
    position: relative;
    width: 520px; height: 298px;
    background: var(--paper);
    border-bottom: 3px solid var(--edge);
    box-shadow: 0 10px 24px rgba(0,0,0,.18);
  }
  /* front */
  .card-front .brand {
    position: absolute; left: 0; right: 0; top: 70px;
    display: flex; align-items: center; justify-content: center; gap: 14px;
  }
  .brand-square {
    width: 34px; height: 34px;
    border: 2px solid var(--amber);
  }
  .brand-name {
    font-size: 19px; font-weight: 400; letter-spacing: .22em;
    color: var(--ink); text-transform: uppercase;
  }
  .card-front .rule {
    position: absolute; left: 130px; right: 130px; top: 126px;
    height: 1px; background: var(--ink);
  }
  .contact {
    position: absolute; left: 0; right: 0; top: 158px;
    display: flex; justify-content: center; gap: 18px;
  }
  .contact-person { text-align: right; }
  .person-name {
    font-size: 20px; font-weight: 700; color: var(--amber);
    text-transform: uppercase; letter-spacing: .01em; line-height: 1.15;
  }
  .contact-line { font-size: 14px; color: var(--ink-soft); line-height: 1.4; }
  .divider { width: 1px; background: var(--ink-soft); margin-top: 22px; height: 34px; }
  .contact-company { padding-top: 22px; }
  /* back */
  .card-back .brand {
    position: absolute; left: 0; right: 0; top: 108px;
    display: flex; flex-direction: column; align-items: center; gap: 16px;
  }
  .card-back .brand-square { width: 58px; height: 58px; border-width: 3px; }
  .card-back .brand-name { font-size: 17px; }
  .back-web {
    position: absolute; right: 24px; bottom: 18px;
    font-size: 11px; letter-spacing: .12em; color: var(--ink);
  }
</style>
</head>
<body>
  <main class="stage">
    <section class="card card-front" aria-label="Card front">
      <div class="brand">
        <span class="brand-square"></span>
        <span class="brand-name">Stonehaven Custom Builders</span>
      </div>
      <div class="rule"></div>
      <div class="contact">
        <div class="contact-person">
          <p class="person-name">Colin Marsh</p>
          <p class="contact-line">ColinMarshSCB@quillpost.net</p>
        </div>
        <span class="divider"></span>
        <div class="contact-company">
          <p class="contact-line">P-208-637-4120</p>
          <p class="contact-line">Stonehavencustombuilders.com</p>
        </div>
      </div>
    </section>
    <section class="card card-back" aria-label="Card back">
      <div class="brand">
        <span class="brand-square"></span>
        <span class="brand-name">Stonehaven Custom Builders</span>
      </div>
      <p class="back-web">Stonehavencustombuilders.com</p>
    </section>
  </main>
</body>
</html>
```